Astrologer needs a design for business card

I need a business card design for my job in astrology and flower therapy.
In front side need the information add file.

In back side need the informations above:
INTERPRETAÇÕES
TENDÊNCIAS
AUTOCONHECIMENTO
ANÁLISE VOCACIONAL
DIRECIONAMENTO DE CARREIRA
RELACIONAMENTOS
ASTROLOGIA EMPRESARIAL
TERAPIA FLORAL – Florias de Drues e Davi Quirelo

Industry/Entity Type

Business

Logo Text

NEVU

```html
<!DOCTYPE html>
<html lang="pt">
<head>
<meta charset="utf-8">
<title>Lívia Montenor – astrologia e florais</title>
<link href="https://fonts.googleapis.com/css2?family=Questrial&display=swap" rel="stylesheet">
<style>
  :root {
    --cream: #ede2c9;
    --cream-light: #f3eadb;
    --pattern-tone: #e4d6b9;
    --wine: #7a1d20;
    --wine-dark: #5e1316;
    --band-line: #c9a98f;
    --ink: #2f241c;
    --white: #fdf8f0;
    --floral-brown: #7d5a3c;
    --floral-pink: #d99a92;
  }
  * { margin: 0; padding: 0; box-sizing: border-box; }
  html, body { width: 1200px; height: 350px; overflow: hidden; background: #ffffff; }
  body { font-family: "Questrial", sans-serif; color: var(--ink); }

  .card-sheet { position: relative; width: 1200px; height: 350px; display: flex; }

  .card-front, .card-back { position: relative; width: 600px; height: 350px; overflow: hidden; }
  .card-front { background: var(--cream); }
  .card-back {
    background: radial-gradient(ellipse at 50% 50%, var(--cream-light), var(--pattern-tone));
    border-left: 1px solid #f7f0e3;
  }

  .band {
    position: absolute; left: 0; right: 0; top: 118px; height: 124px;
    background: var(--wine);
    border-top: 2px solid var(--band-line);
    border-bottom: 2px solid var(--band-line);
    box-shadow: inset 0 0 0 3px var(--wine-dark);
  }

  .floral-top {
    position: absolute; left: 420px; top: 0; width: 180px; height: 118px;
    background: radial-gradient(ellipse at 55% 35%, rgba(125,90,60,0.35), rgba(125,90,60,0) 70%);
  }
  .floral-corner {
    position: absolute; left: 0; top: 96px; width: 240px; height: 254px;
    background:
      radial-gradient(ellipse at 30% 70%, rgba(217,154,146,0.55), rgba(217,154,146,0) 55%),
      radial-gradient(ellipse at 15% 40%, rgba(125,90,60,0.35), rgba(125,90,60,0) 65%);
  }

  .contact { position: absolute; left: 36px; top: 52px; font-size: 15px; line-height: 24px; }

  .brand { position: absolute; left: 150px; top: 138px; width: 310px; text-align: center; color: var(--white); }
  .brand-name { font-size: 36px; line-height: 40px; letter-spacing: 1px; }
  .brand-tagline { font-size: 19px; line-height: 24px; margin-top: 4px; }

  .address { position: absolute; right: 36px; top: 250px; text-align: right; font-size: 15px; line-height: 24px; }

  .services { position: absolute; left: 0; top: 0; width: 600px; height: 350px; color: var(--white); font-size: 15px; text-transform: none; }
  .service-row { position: absolute; left: 42px; display: flex; align-items: center; white-space: nowrap; }
  .service-row .col-a { width: 172px; }
  .service-row .divider { display: inline-block; width: 2px; height: 14px; background: var(--white); margin: 0 8px; }
  .row-1 { top: 130px; } .row-2 { top: 162px; } .row-3 { top: 194px; }
</style>
</head>
<body>
  <main class="card-sheet">
    <section class="card-front">
      <div class="band"></div>
      <div class="floral-top" role="img" aria-label="Ramagem floral em tons de marrom descendo do canto superior"></div>
      <div class="floral-corner" role="img" aria-label="Arranjo de flores rosadas com ramos espiralados no canto inferior esquerdo"></div>

      <div class="contact">
        <p>liviamontenor@mailnest.com</p>
        <p>(51) 9000-2718</p>
      </div>

      <div class="brand">
        <p class="brand-name">Lívia Montenor</p>
        <p class="brand-tagline">- astrologia e florais -</p>
      </div>

      <address class="address" style="font-style: normal;">
        <p>Av. das Acácias, 218</p>
        <p>Casa 07 – Vila Serena</p>
        <p>– RS – 90.000-120</p>
      </address>
    </section>

    <section class="card-back" role="img" aria-label="Fundo creme com padrão damasco suave">
      <div class="band"></div>
      <div class="services">
        <div class="service-row row-1"><span class="col-a">RELACIONAMENTOS</span><span class="divider"></span><span>ASTROLOGIA EMPRESARIAL</span><span class="divider"></span><span>INTERPRETAÇÕES</span></div>
        <div class="service-row row-2"><span class="col-a">ANÁLISE VOCACIONAL</span><span class="divider"></span><span>TENDÊNCIAS</span><span class="divider"></span><span>DIRECIONAMENTO DE CARREIRA</span></div>
        <div class="service-row row-3"><span class="col-a">AUTOCONHECIMENTO</span><span class="divider"></span><span>TERAPIA FLORAL – Florias de Drues e Davi Quirelo</span></div>
      </div>
    </section>
  </main>
</body>
</html>
```